Velmira Body Oil Label for 4 -8 oz bottles

We are selling 4 and 8 oz body oils and need a label to put on our bottles. I'm not sure if we want a label for the front and also the back of the bottle or just one label in the front. You can give me examples of each way. Attached is our logo on a blue background but the background will change colors depending on the scent as specified in the design description. Our bottle will be either clear or white with a pump spray type lid as shown in the attached example. Attached are also our design criteria which is needed for the labels.
Updates

We have decided to use the disc top cap and not the pump spray cap. If you are able to, please show us the design on the 4 oz bottle with the disc top cap. Thanks

Target Market(s)

women

Industry/Entity Type

skincare, cosmetics

Font styles to use
Serif
Sans Serif

Requirements
Must have
• stylish name for each scented oil which contrasts the font in the logo. Also must have darker colors since the logo colors are lighter.
Nice to have
• Border around the labels, maybe one solid color or maybe two complimenting colors which go well with the fragrnace name
Should not have
• background colors that match the logo colors

```html
<!DOCTYPE html>
<html lang="en">
<head>
<meta charset="utf-8">
<title>Velmira Body Oil Label</title>
<link rel="stylesheet" href="https://fonts.googleapis.com/css2?family=Montserrat:wght@300;400;500;600;700&family=Caveat+Brush&display=swap">
<style>
  :root {
    --page-bg: #e9e9e9;
    --label-light: #7bbbdd;
    --label-mid: #6aa8cf;
    --label-dark: #4b80a5;
    --ink: #ffffff;
    --ink-soft: rgba(255, 255, 255, 0.92);
  }
  * { margin: 0; padding: 0; box-sizing: border-box; }
  html, body {
    width: 1200px;
    height: 800px;
    overflow: hidden;
    background: var(--page-bg);
  }
  .canvas {
    position: relative;
    width: 1200px;
    height: 800px;
    background: var(--page-bg);
  }
  .label {
    position: absolute;
    left: 460px;
    top: 19px;
    width: 280px;
    height: 762px;
    background: linear-gradient(90deg, var(--label-light) 0%, var(--label-mid) 45%, var(--label-dark) 100%);
    color: var(--ink);
    font-family: "Montserrat", sans-serif;
  }
  .brand {
    position: absolute;
    top: 150px;
    left: 0;
    width: 100%;
    text-align: center;
    font-size: 40px;
    font-weight: 400;
    letter-spacing: 1px;
    line-height: 48px;
    color: var(--ink);
  }
  .product-line {
    position: absolute;
    top: 204px;
    left: 138px;
    font-size: 12px;
    font-weight: 300;
    letter-spacing: 3px;
    line-height: 14px;
    color: var(--ink);
  }
  .claims {
    position: absolute;
    top: 334px;
    left: 0;
    width: 272px;
    text-align: center;
    font-size: 10.5px;
    line-height: 14px;
    font-weight: 400;
    color: var(--ink-soft);
  }
  .ingredients {
    position: absolute;
    top: 384px;
    left: 55px;
    width: 190px;
    font-size: 6.6px;
    line-height: 10.8px;
    color: var(--ink-soft);
  }
  .section-title {
    font-weight: 700;
    display: block;
  }
  .tagline {
    position: absolute;
    top: 466px;
    left: 55px;
    font-family: "Caveat Brush", cursive;
    font-size: 22px;
    color: var(--ink);
    transform: skewX(-4deg);
  }
  .warnings {
    position: absolute;
    top: 520px;
    left: 55px;
    width: 190px;
    font-size: 6.8px;
    line-height: 10.4px;
    color: var(--ink-soft);
  }
  .warnings-list {
    list-style: none;
    padding: 0;
    margin: 0;
  }
  .warnings-list li::before { content: "· "; }
  .distributor {
    position: absolute;
    top: 641px;
    left: 55px;
    width: 200px;
    font-size: 6.6px;
    line-height: 11px;
    font-weight: 600;
    color: var(--ink-soft);
  }
  .origin {
    position: absolute;
    top: 693px;
    left: 55px;
    font-size: 12.5px;
    font-weight: 500;
    word-spacing: 3px;
  }
  .net-weight {
    position: absolute;
    top: 718px;
    left: 139px;
    font-size: 7px;
    color: var(--ink-soft);
  }
</style>
</head>
<body>
  <main class="canvas">
    <section class="label">
      <h1 class="brand">Velmira</h1>
      <p class="product-line">BODY OILS</p>

      <p class="claims">Non-Greesy<br>With Vitamin E<br>Ultra Moisturizing</p>

      <p class="ingredients">
        <span class="section-title">Ingredients:</span>
        Cocos Nucifera (Coconut) Oil, Prunus Amygdalus Dulcis (Almond) Oil, Vitis Vinifera (Grapeseed) Oil, Sesamum Indicum (Sesame) Seed Oil, Simmondsia Chinensis (Jojoba) Oil, Tocopheryl Acetate (Vitamin E). Essential oils, and fragrances
      </p>

      <p class="tagline">Use daily for best results.</p>

      <div class="warnings">
        <span class="section-title">WARNINGS / DISCLAIMERS:</span>
        <ul class="warnings-list">
          <li>For external use only.</li>
          <li>Avoid contact with eyes.</li>
          <li>Discontinue use if irritation occurs.</li>
          <li>Keep out of reach of children.</li>
          <li>Contains nut oils</li>
          <li>use with caution if you have nut allergies.</li>
        </ul>
      </div>

      <p class="distributor">Distributed by Velmira 412 Aspen Ridge Lane<br>Cedar Falls, CO 80000</p>

      <p class="origin">Made in USA</p>
      <p class="net-weight">Net Wt. 4 fl. oz. (118 mL)</p>
    </section>
  </main>
</body>
</html>
```